Business letterhead and powerpoint template

Hi, I have recently started using a new logo (found through MarkVesta) and would now like to use that logo for letterheads and powerpoint.

Attached is the logo and one version of a brochure I have recently used.

Business

```html
<!DOCTYPE html>
<html lang="en">
<head>
<meta charset="utf-8">
<title>Harbourline Capital Letterhead</title>
<link rel="stylesheet" href="https://fonts.googleapis.com/css2?family=Open+Sans:wght@400&display=swap">
<style>
  :root {
    --ink: #231f20;
    --ink-soft: #3a3a3a;
    --rule: #c9c9c9;
    --accent: #ef5124;
    --paper-top: #ffffff;
    --paper-bottom: #efeff1;
    --white: #ffffff;
  }
  * { margin: 0; padding: 0; box-sizing: border-box; }
  html, body { width: 933px; height: 1200px; overflow: hidden; }
  body { font-family: "Open Sans", Arial, sans-serif; color: var(--ink); }

  .letterhead {
    position: relative;
    width: 933px;
    height: 1200px;
    background: linear-gradient(160deg, var(--paper-top) 30%, var(--paper-bottom) 100%);
  }

  .brand {
    position: absolute;
    left: 32px;
    top: 74px;
    display: flex;
    align-items: center;
    gap: 12px;
  }
  .brand-mark {
    width: 22px;
    height: 22px;
    background: var(--accent);
  }
  .brand-name {
    font-size: 36px;
    font-weight: 400;
    letter-spacing: 1px;
    color: var(--ink);
    line-height: 1;
  }

  .contact {
    position: absolute;
    left: 703px;
    top: 56px;
    padding-left: 12px;
    border-left: 1px solid var(--rule);
    font-size: 14.5px;
    color: var(--ink-soft);
    line-height: 24px;
  }
  .contact-line { display: flex; align-items: center; gap: 6px; }
  .contact-line svg { width: 12px; height: 12px; fill: var(--ink-soft); }

  .address {
    position: absolute;
    left: 24px;
    top: 1153px;
    display: flex;
    align-items: center;
    gap: 6px;
    font-size: 13.5px;
    color: var(--ink);
  }
  .address svg { width: 14px; height: 12px; }

  .footer-band {
    position: absolute;
    left: 0;
    top: 1152px;
    width: 933px;
    height: 48px;
  }
  .website {
    position: absolute;
    right: 36px;
    top: 1165px;
    font-size: 14.5px;
    color: var(--white);
  }
</style>
</head>
<body>
  <div class="letterhead">
    <div class="brand">
      <span class="brand-mark"></span>
      <span class="brand-name">Harbourline Capital</span>
    </div>

    <div class="contact">
      <div class="contact-line">
        <svg viewBox="0 0 12 12" aria-hidden="true"><path d="M2.5 1 L4.5 1 L5.3 3.4 L4 4.4 C4.6 5.9 6 7.3 7.6 8 L8.6 6.7 L11 7.5 L11 9.5 C11 10.4 10.3 11 9.4 11 C4.8 10.7 1.3 7.2 1 2.6 C1 1.7 1.6 1 2.5 1 Z"/></svg>
        <span>+61 (0)2 9410 3572</span>
      </div>
      <div class="contact-line">
        <svg viewBox="0 0 12 12" aria-hidden="true"><rect x="3" y="1" width="6" height="4"/><rect x="1" y="5" width="10" height="5" rx="1"/><rect x="3" y="8" width="6" height="3" fill="#fff"/></svg>
        <span>+61 (0)2 9410 3500</span>
      </div>
    </div>

    <div class="address">
      <svg viewBox="0 0 14 12" aria-hidden="true"><path d="M1 5 L7 1 L13 5 Z" fill="#ef5124"/><rect x="1" y="6" width="12" height="1.5" fill="#ef5124"/><rect x="1" y="8.5" width="12" height="1.5" fill="#ef5124"/><rect x="1" y="10.5" width="12" height="1.5" fill="#ef5124"/></svg>
      <span>Level 9 Suite 4 28 Ridgeway Lane Harbour Point 2000 NSW Australia</span>
    </div>

    <svg class="footer-band" viewBox="0 0 933 48" preserveAspectRatio="none" aria-hidden="true">
      <path d="M0 27 H610 C628 27 634 31 622 34 H0 Z" fill="#231f20"/>
      <path d="M0 34 H600 C628 34 628 10 672 10 H933 V48 H0 Z" fill="#ef5124"/>
    </svg>
    <div class="website">www.harbourlinecapital.com.au</div>
  </div>
</body>
</html>
```